Web Developer Needs a Business Card Design

I need a personal business card design that represents me as a web developer for potential employers. I would like the background to be a dark color on the front for contrast with my logo and name. The back will have all my information along with a smaller version of the logo. I want something with a modern look and feel, not too conservative. This will be used for potential employers and freelance work.

Industry/Entity Type

Business

Contact Information for Business Card

Front should have my logo and name. The back should have all my personal information which would include: name: Tom Brevardi, phone: 570-614-9083, email: tombrevardi@mailwisp.com, website url: www.tombrevardi.com, logo, web developer.

Font styles to use
Sans Serif

Requirements
Must have
• Must include my logo. The color palette base color will be the logo color.

```html
<!DOCTYPE html>
<html lang="en">
<head>
<meta charset="utf-8">
<title>Tom Brevardi — Business Card</title>
<link href="https://fonts.googleapis.com/css2?family=Questrial&family=Source+Sans+3:wght@400;600&display=swap" rel="stylesheet">
<style>
  :root {
    --teal: #7ccbbd;
    --ink: #111111;
    --paper: #f7f7f7;
    --card-black: #050505;
    --backdrop: #e4e4e2;
  }
  * { box-sizing: border-box; margin: 0; padding: 0; }
  html, body { width: 1200px; height: 780px; overflow: hidden; }
  body {
    background: var(--backdrop);
    display: flex;
    align-items: center;
    justify-content: center;
    gap: 60px;
  }
  .card {
    position: relative;
    width: 500px;
    height: 286px;
    overflow: hidden;
    box-shadow: 0 10px 26px rgba(0,0,0,.18);
  }

  /* Shared mark */
  .mark {
    position: absolute;
    border-radius: 50%;
    border: 10px solid var(--teal);
    display: flex;
    align-items: center;
    justify-content: center;
  }
  .mark-name {
    font-family: "Questrial", sans-serif;
    color: var(--teal);
    text-transform: uppercase;
    letter-spacing: .5px;
  }

  /* Contact side */
  .card-contact { background: var(--paper); }
  .card-contact .mark {
    left: 52px; top: 68px; width: 150px; height: 150px;
  }
  .card-contact .mark-name { font-size: 19px; }
  .contact-block {
    position: absolute;
    left: 235px; top: 62px;
  }
  .person-name {
    font-family: "Questrial", sans-serif;
    font-size: 27px;
    color: var(--teal);
    text-transform: uppercase;
    line-height: 1;
  }
  .person-title {
    font-family: "Source Sans 3", sans-serif;
    font-weight: 600;
    font-size: 15px;
    color: var(--ink);
    margin-top: 4px;
  }
  .contact-list { list-style: none; margin-top: 30px; }
  .contact-item {
    display: flex;
    align-items: center;
    gap: 10px;
    font-family: "Source Sans 3", sans-serif;
    font-weight: 600;
    font-size: 16px;
    color: var(--ink);
    height: 30px;
  }
  .contact-icon {
    width: 20px; height: 20px;
    border-radius: 50%;
    background: var(--teal);
    display: flex; align-items: center; justify-content: center;
    flex: none;
  }
  .contact-icon svg { width: 11px; height: 11px; }

  /* Name side */
  .card-name { background: var(--card-black); }
  .stripe {
    position: absolute;
    left: 0; right: 0;
    height: 7px;
    background: var(--teal);
  }
  .stripe-top { top: 92px; }
  .stripe-bottom { top: 187px; }
  .name-band {
    position: absolute;
    left: 0; right: 0;
    top: 107px; height: 72px;
    background: var(--paper);
    display: flex;
    align-items: center;
    padding-left: 262px;
  }
  .name-band .person-name { font-size: 29px; letter-spacing: 1px; }
  .mark-disc {
    position: absolute;
    left: 18px; top: 28px;
    width: 230px; height: 230px;
    border-radius: 50%;
    background: var(--paper);
  }
  .card-name .mark {
    left: 33px; top: 43px; width: 200px; height: 200px;
    border-width: 11px;
  }
  .card-name .mark-name { font-size: 24px; }
</style>
</head>
<body>

  <section class="card card-contact" aria-label="Card back with contact details">
    <div class="mark"><span class="mark-name">Brevardi</span></div>
    <div class="contact-block">
      <h1 class="person-name">Tom Brevardi</h1>
      <p class="person-title">Web Developer</p>
      <ul class="contact-list">
        <li class="contact-item">
          <span class="contact-icon">
            <svg viewBox="0 0 12 12"><path d="M2.5 1h2l1 2.6-1.3 1a6 6 0 0 0 3.2 3.2l1-1.3L11 7.5v2a1.2 1.2 0 0 1-1.3 1.2A9 9 0 0 1 1.3 2.3 1.2 1.2 0 0 1 2.5 1z" fill="#fff"/></svg>
          </span>
          570-614-9083
        </li>
        <li class="contact-item">
          <span class="contact-icon">
            <svg viewBox="0 0 12 12"><rect x="1" y="2.5" width="10" height="7" fill="#fff"/><path d="M1 2.5l5 4 5-4" fill="none" stroke="#7ccbbd" stroke-width="1"/></svg>
          </span>
          tombrevardi@mailwisp.com
        </li>
        <li class="contact-item">
          <span class="contact-icon">
            <svg viewBox="0 0 12 12"><circle cx="6" cy="6" r="4.5" fill="none" stroke="#fff" stroke-width="1.2"/><path d="M1.5 6h9M6 1.5c-2 2.5-2 6.5 0 9M6 1.5c2 2.5 2 6.5 0 9" fill="none" stroke="#fff" stroke-width="1"/></svg>
          </span>
          www.tombrevardi.com
        </li>
      </ul>
    </div>
  </section>

  <section class="card card-name" aria-label="Card front with name">
    <div class="stripe stripe-top"></div>
    <div class="stripe stripe-bottom"></div>
    <div class="name-band"><h2 class="person-name">Tom Brevardi</h2></div>
    <div class="mark-disc"></div>
    <div class="mark"><span class="mark-name">Brevardi</span></div>
  </section>

</body>
</html>
```